New emergency medical service needs a marketing flyer for prospective customers

We need a tri fold brochure on an 8.5 X 11 stock for a new emergency medical service in Pennsylvania. We provide basic first aid and now Covid-19 pre screening and temperature monitoring for special events, large gatherings and businesses. Examples of these would be but not limited to: Sporting events, carnivals, festivals, craft shows, warehouses, churches, manufacturing facilities, industrial buildings, large construction sites, multi occupancy officer buildings. The market for this is pretty much untouched and endless. we would like to use gray as the back ground color and obviously our logo. The final design should grab their attention and communicate the importance of having trained and certified professionals at their event or facility. We want to give them that piece of mind they are in good hands with us.

Target Market(s)

primary focus is going to be on businesses with large offices, large buildings or lots of foot traffic in and out of the building

Requirements
Must have
• gray background, pictures, company phone # , company web site, and contact email address. I will provide all that information to the winner to add at the end.
Nice to have
• pictures that covers the whole front cover with logo at top

```html
<!DOCTYPE html>
<html lang="en">
<head>
<meta charset="utf-8">
<title>Keystone Medical Services – Tri-fold Brochure</title>
<link href="https://fonts.googleapis.com/css2?family=Roboto:wght@400;500;700&family=Source+Sans+3:wght@400;600;700&family=Merriweather:ital,wght@1,400;1,700&display=swap" rel="stylesheet">
<style>
:root{
  --blue:#2d3192;
  --blue-dark:#20236e;
  --page:#d4d5d7;
  --panel-dark:#3b3b3d;
  --panel-mid:#6d6e71;
  --ink:#3a3a3c;
  --white:#ffffff;
}
*{margin:0;padding:0;box-sizing:border-box}
html,body{width:927px;height:1200px;overflow:hidden;background:var(--page)}
body{position:relative;font-family:"Source Sans 3",Arial,sans-serif;color:var(--ink)}
.sheet{position:absolute;width:655px;height:509px;overflow:hidden;box-shadow:0 10px 12px -6px rgba(0,0,0,.45)}
.sheet--outside{left:122px;top:54px}
.sheet--inside{left:123px;top:616px;width:657px}
.panel{position:absolute;top:0;height:100%;overflow:hidden}
.photo{position:absolute}
.abs{position:absolute}

/* outside: left panel */
.p-intro{left:0;width:214px;background:linear-gradient(180deg,#fff 60%,#eeeeef)}
.p-intro .photo{left:0;top:0;width:214px;height:216px;background:linear-gradient(135deg,#c9d4de,#8fa6bd 45%,#e8eaec 70%,#c4453d)}
.intro-text{left:12px;top:229px;width:196px;font-size:8.8px;line-height:1.25;letter-spacing:-.15px}
.intro-list{list-style:none;margin-top:4px}
.intro-list li{line-height:14px}
.intro-list li::before{content:"• "}
.pill{position:absolute;background:var(--blue);color:#fff;border-radius:11px;display:flex;align-items:center;justify-content:center;gap:5px;font-family:"Roboto",Arial,sans-serif;font-weight:500;letter-spacing:1.2px;white-space:nowrap}
.intro-phone{left:34px;top:391px;width:147px;height:18px;font-size:11px}
.peace{left:0;width:214px;text-align:center;font-family:"Merriweather",Georgia,serif;font-style:italic}
.peace-title{top:425px;color:var(--blue);font-size:13px;font-weight:700}
.peace-line{top:445px;font-size:10.5px;color:#4a4a4c}

/* outside: middle panel */
.p-contact{left:214px;width:216px;background:linear-gradient(180deg,#49494b,var(--panel-dark) 40%,#2e2e30)}
.ring{position:absolute;left:50px;top:48px;width:114px;height:114px;border-radius:50%;background:#6b6b6d;padding:7px}
.ring .photo{position:static;width:100%;height:100%;border-radius:50%;background:radial-gradient(circle at 40% 70%,#c33 0,#8a2a2a 20%,#2a2a2c 45%,#6f8c5b 75%)}
.brand{font-family:"Roboto",Arial,sans-serif;font-weight:500;display:flex;align-items:center;gap:6px;white-space:nowrap}
.brand-mark{width:12px;height:12px;border-radius:50%;background:currentColor;flex:none}
.brand--light{color:#fff}
.brand--blue{color:var(--blue)}
.contact-brand{left:0;width:216px;top:205px;justify-content:center;font-size:19px}
.contact-head{left:0;width:216px;top:289px;text-align:center;color:#f0f0f0;font-family:"Roboto",Arial,sans-serif;font-weight:500;font-size:10px;line-height:16.5px;letter-spacing:.3px}
.contact-btn{left:34px;top:354px;width:148px;height:18px;border-radius:9px;background:#b8b9bb;color:var(--blue);font-family:"Roboto",Arial,sans-serif;font-weight:700;font-size:12px;display:flex;align-items:center;justify-content:center}
.contact-lines{left:0;width:216px;top:385px;text-align:center;color:#fff;font-size:10.5px;line-height:19px;letter-spacing:.3px}

/* outside: right panel (cover) */
.p-cover{left:430px;width:225px;background:#fff}
.cover-brand{left:0;width:225px;top:30px;justify-content:center;font-size:21px}
.p-cover .photo{left:0;top:60px;width:225px;height:335px;background:linear-gradient(160deg,#b7c3cf,#4a5f8c 35%,#1f2f66 65%,#2a3c6e)}
.badge{position:absolute;left:158px;top:318px;width:62px;height:62px;border-radius:50%;background:#3a4f86;border:3px solid #c9ccd3}
.cover-head{left:0;width:225px;top:406px;text-align:center;font-family:"Roboto",Arial,sans-serif;font-weight:500;font-size:14.5px;line-height:19.5px;color:#555557;letter-spacing:.3px}
.cover-head strong{color:var(--blue);font-weight:700}

.sheet-wave{left:0;top:0}
.band{position:absolute;left:0;top:481px;width:655px;height:28px;background:linear-gradient(180deg,var(--blue),var(--blue-dark));display:flex;color:#fff;font-family:"Roboto",Arial,sans-serif;font-size:10.5px;letter-spacing:1px}
.band span{display:flex;align-items:center;justify-content:center;gap:5px}

/* inside: left panel */
.p-services{left:0;width:219px;background:linear-gradient(180deg,#a3a4a7,var(--panel-mid) 45%,#555558)}
.tab{position:absolute;height:25px;background:var(--blue);color:#fff;border-radius:0 13px 13px 0;font-family:"Roboto",Arial,sans-serif;font-weight:500;font-size:12.5px;display:flex;align-items:center;padding-left:12px;box-shadow:0 2px 3px rgba(0,0,0,.35)}
.services-tab{left:0;top:33px;width:180px}
.body-copy{color:#f2f2f2;font-size:8.8px;line-height:11.4px;text-align:justify;letter-spacing:-.1px}
.body-copy p+p{margin-top:10px}
.services-copy{left:13px;top:74px;width:192px}
.services-photo{left:0;top:300px;width:219px;height:209px;background:linear-gradient(150deg,#9a8a80,#cdb7a4 40%,#3d4450 75%,#a33)}
.services-ring{position:absolute;left:103px;top:242px;width:108px;height:108px;border-radius:50%;background:#8e8f92;padding:5px}
.services-ring .photo{position:static;width:100%;height:100%;border-radius:50%;background:radial-gradient(circle at 50% 40%,#e6edf3,#7e9cb7 55%,#3d5b82)}

/* inside: middle panel */
.p-emergency{left:219px;width:216px;background:linear-gradient(90deg,#e6e6e7,#fafafa 30%,#fafafa 75%,#e3e3e4)}
.emergency-brand{left:0;width:216px;top:35px;justify-content:center;font-size:21px}
.emergency-title{left:20px;top:90px;color:var(--blue);font-family:"Roboto",Arial,sans-serif;font-weight:500;font-size:12.5px;letter-spacing:.2px}
.service{position:absolute;left:8px;width:200px;display:flex;gap:10px}
.service-icon{width:46px;height:46px;border-radius:50%;background:#fff;border:3px solid #d6d6d8;flex:none;display:flex;align-items:center;justify-content:center;box-shadow:0 2px 3px rgba(0,0,0,.15)}
.service h3{color:var(--blue);font-family:"Roboto",Arial,sans-serif;font-weight:500;font-size:8.7px;margin:4px 0 2px}
.service p{font-size:7.2px;line-height:8.6px;color:#444;text-align:justify}
.emergency-call{left:11px;top:463px;width:186px;height:19px;font-size:11px;font-weight:400}
.emergency-url{left:0;width:216px;top:488px;text-align:center;font-family:"Roboto",Arial,sans-serif;font-size:11px;letter-spacing:1px;color:#333}

/* inside: right panel */
.p-community{left:435px;width:222px;background:linear-gradient(180deg,#8d8e91,var(--panel-mid) 40%,#58585b)}
.community-photo{left:0;top:0;width:222px;height:212px;background:linear-gradient(160deg,#9bb06e,#e9ecef 35%,#c7ccd3 60%,#7e8794)}
.community-ring{position:absolute;left:103px;top:133px;width:108px;height:108px;border-radius:50%;background:#a9aaad;padding:5px}
.community-ring .photo{position:static;width:100%;height:100%;border-radius:50%;background:radial-gradient(circle at 50% 60%,#c0392b,#6f8f4b 45%,#a9c98a)}
.community-tab{left:1px;top:247px;width:180px}
.community-copy{left:12px;top:287px;width:200px}
</style>
</head>
<body>

<section class="sheet sheet--outside">
  <div class="panel p-intro">
    <div class="photo" role="img" aria-label="Medic in protective gown working inside an ambulance"></div>
    <div class="abs intro-text">
      <p>We provide basic first aid and now Covid-19 pre screening and temperature monitoring for:</p>
      <ul class="intro-list">
        <li>Special Events</li><li>Large Gatherings</li><li>Businesses</li><li>Sporting Events</li>
        <li>Manufacturing Facilities</li><li>Industrial Buildings</li><li>Large Construction Sites</li>
        <li>Multi Occupancy Officer Buildings</li>
      </ul>
    </div>
    <div class="pill intro-phone">
      <svg width="10" height="10" viewBox="0 0 24 24"><circle cx="12" cy="12" r="10" fill="none" stroke="#fff" stroke-width="2.4"/><path fill="#fff" d="M8 7c1 0 1.5 2 1.5 2.5S8.8 10.5 9 11c.5 1.3 2.2 3 3.5 3.5.5.2.8-.7 1.3-.7s2.5.7 2.5 1.5-1 2-2 2C10.5 17.3 6.7 13.5 6.5 10c0-1.5 1-3 1.5-3z"/></svg>
      0100 555 0199
    </div>
    <div class="abs peace peace-title">Piece of Mind</div>
    <div class="abs peace peace-line">you are in good hands with us!</div>
  </div>

  <div class="panel p-contact">
    <div class="ring"><div class="photo" role="img" aria-label="Responder carrying a red medical response bag at an outdoor event"></div></div>
    <div class="abs brand brand--light contact-brand"><span class="brand-mark"></span>Keystone Medical</div>
    <div class="abs contact-head">FOR MORE INFORMATION ABOUT<br>SPECIAL EVENT PLANNING<br>PLEASE CONTACT US:</div>
    <div class="abs contact-btn">CONTACT US</div>
    <div class="abs contact-lines">0100 555 0199<br>info@keystonemedical.example<br>1234 Name of Street<br>Maple Grove, Northland</div>
  </div>

  <div class="panel p-cover">
    <div class="photo" role="img" aria-label="Masked paramedic giving oxygen to a patient in an ambulance"></div>
    <div class="badge" role="img" aria-label="Service badge"></div>
    <div class="abs cover-head">PROVIDING HEALTH AND<br>SAFETY NEEDS FOR<br><strong>FIRST AID AND COVID-19</strong></div>
  </div>

  <svg class="abs sheet-wave" width="655" height="140" viewBox="0 0 655 140" aria-hidden="true">
    <path d="M430 0 H655 V96 C560 104 500 92 430 70 Z" fill="#fff"/>
    <path d="M430 70 C500 92 560 104 655 96 V112 C560 122 500 110 430 84 Z" fill="#c9cacc" opacity=".7"/>
    <path d="M0 58 C100 20 250 14 360 36 C450 56 540 100 655 90 V100 C540 110 450 68 360 46 C250 24 100 30 0 70 Z" fill="var(--blue)"/>
  </svg>

  <div class="abs brand brand--blue cover-brand" style="left:430px"><span class="brand-mark"></span>Keystone Medical</div>

  <div class="band">
    <span style="width:214px">www.keystonemedical.example</span>
    <span style="width:216px"><svg width="10" height="10" viewBox="0 0 24 24"><circle cx="12" cy="12" r="10" fill="none" stroke="#fff" stroke-width="2.4"/><path fill="#fff" d="M8 7c1 0 1.5 2 1.5 2.5S8.8 10.5 9 11c.5 1.3 2.2 3 3.5 3.5.5.2.8-.7 1.3-.7s2.5.7 2.5 1.5-1 2-2 2C10.5 17.3 6.7 13.5 6.5 10c0-1.5 1-3 1.5-3z"/></svg>0100 555 0199</span>
    <span style="width:225px">www.keystonemedical.example</span>
  </div>
</section>

<section class="sheet sheet--inside">
  <div class="panel p-services">
    <div class="tab services-tab">MEDICAL SERVICES</div>
    <div class="abs body-copy services-copy">
      <p>At Keystone we have a broad range of Health and Safety classes to suit your every need. We take pride in our instructors who have years of experience instructing quality built classes.</p>
      <p>We make learning CPR fun and affordable for the everyday public and healthcare providers.</p>
      <p>All CPR instruction follows the National Cardiac Council and National Safety and Health Institute formats. The leaders in cardiac research.</p>
      <p>We can adjust any course format to suit your CPR and First Aid needs.</p>
    </div>
    <div class="photo services-photo" role="img" aria-label="Gloved hands performing CPR chest compressions on a training manikin"></div>
    <svg class="abs" style="left:0;top:270px" width="219" height="80" viewBox="0 0 219 80" aria-hidden="true">
      <path d="M0 26 C80 18 160 30 219 70 L219 78 C160 40 80 30 0 34 Z" fill="var(--blue)"/>
    </svg>
    <div class="services-ring"><div class="photo" role="img" aria-label="Lab worker in face shield handling test samples"></div></div>
  </div>

  <div class="panel p-emergency">
    <div class="abs brand brand--blue emergency-brand"><span class="brand-mark"></span>Keystone Medical</div>
    <div class="abs emergency-title">EMERGENCY DEPARTMENT</div>

    <div class="service" style="top:146px">
      <div class="service-icon"><svg width="22" height="22" viewBox="0 0 24 24"><rect x="2" y="6" width="20" height="15" rx="2" fill="var(--blue)"/><rect x="8" y="3" width="8" height="4" rx="1" fill="none" stroke="var(--blue)" stroke-width="2"/><path d="M12 9v9M7.5 13.5h9" stroke="#fff" stroke-width="2.6"/></svg></div>
      <div><h3>Main Emergency Department</h3><p>for ill or injured patients with complex or serious conditions</p></div>
    </div>
    <div class="service" style="top:210px">
      <div class="service-icon"><svg width="24" height="24" viewBox="0 0 24 24"><circle cx="12" cy="13" r="8.5" fill="none" stroke="var(--blue)" stroke-width="2"/><path d="M10 2h4M12 2v2.5" stroke="var(--blue)" stroke-width="2"/><path d="M12 9v8M8 13h8" stroke="var(--blue)" stroke-width="2.6"/></svg></div>
      <div><h3>Fast Care</h3><p>for patients with minor ailments including colds, sore throats, small lacerations or cuts, sprains, and simple broken bones</p></div>
    </div>
    <div class="service" style="top:273px">
      <div class="service-icon"><svg width="22" height="22" viewBox="0 0 24 24"><path d="M12 21 3.5 12.5A5 5 0 0 1 12 5.5a5 5 0 0 1 8.5 7Z" fill="var(--blue)"/><path d="M13 8l-3 5h3l-2 5" stroke="#fff" stroke-width="1.6" fill="none"/></svg></div>
      <div><h3>Trauma/Resuscitation</h3><p>Level II Trauma Center for patients with serious injuries</p></div>
    </div>
    <div class="service" style="top:336px">
      <div class="service-icon"><svg width="22" height="22" viewBox="0 0 24 24"><rect x="4" y="4" width="16" height="18" rx="2" fill="none" stroke="var(--blue)" stroke-width="2"/><rect x="9" y="2" width="6" height="4" rx="1" fill="var(--blue)"/><path d="M7 11l1.5 1.5L11 10M7 16l1.5 1.5L11 15M13 11h4M13 16h4" stroke="var(--blue)" stroke-width="1.6" fill="none"/></svg></div>
      <div><h3>Behavioral Health</h3><p>Evaluation and treatment for acute behavioral health issues</p></div>
    </div>
    <div class="service" style="top:400px">
      <div class="service-icon"><svg width="24" height="24" viewBox="0 0 24 24" fill="var(--blue)"><circle cx="9" cy="10" r="4.5"/><circle cx="17" cy="16" r="3"/><circle cx="17" cy="6" r="2"/><path d="M9 3v2.5M9 14.5V17M2 10h2.5M13.5 10H16M4 5l1.8 1.8M12.2 13.2 14 15M17 11.5v1.5M20.5 16H22" stroke="var(--blue)" stroke-width="1.4"/></svg></div>
      <div><h3>Local COVID-19 Responses</h3><p>Preventative measures for best protect EMS personnel, reduce risk, and execute responsible EMS care</p></div>
    </div>

    <div class="pill emergency-call">Call Us
      <svg width="10" height="10" viewBox="0 0 24 24"><circle cx="12" cy="12" r="10" fill="none" stroke="#fff" stroke-width="2.4"/><path fill="#fff" d="M8 7c1 0 1.5 2 1.5 2.5S8.8 10.5 9 11c.5 1.3 2.2 3 3.5 3.5.5.2.8-.7 1.3-.7s2.5.7 2.5 1.5-1 2-2 2C10.5 17.3 6.7 13.5 6.5 10c0-1.5 1-3 1.5-3z"/></svg>
      0100 555 0199</div>
    <div class="abs emergency-url">www.keystonemedical.example</div>
  </div>

  <div class="panel p-community">
    <div class="photo community-photo" role="img" aria-label="White ambulance parked outdoors beside trees"></div>
    <svg class="abs" style="left:0;top:180px" width="222" height="60" viewBox="0 0 222 60" aria-hidden="true">
      <path d="M0 10 C60 34 150 40 222 30 L222 36 C150 46 60 42 0 18 Z" fill="var(--blue)"/>
    </svg>
    <div class="community-ring"><div class="photo" role="img" aria-label="Medic with response bags at a field event"></div></div>
    <div class="tab community-tab">HELPING OUR COMMUNITY</div>
    <div class="abs body-copy community-copy">
      <p>We offer EMS planning and coverage for special events across Central Northland including large sporting events and mass gatherings. We are able to provide a wide range of coverage from a single provider to multiple advanced life support units for gatherings of 500 people to 50,000 people.</p>
      <p>Our Community Paramedicine program helps patients overcome challenges that they may face after being discharged from the hospital. Paramedics will assist patients by ensuring that the patient has filled their prescriptions, verify medications, answer any questions the patient may have, and let the patient's physician know how they are doing.</p>
    </div>
  </div>
</section>

</body>
</html>
```